New Business Card Design Project

Need a design that will create an impact / strong impression towards our clients for our business. We are in the lighting business and we do lighting retrofits for large commercial to industrial clientele.

Target Market(s)

Lighting Industry

Industry/Entity Type

Business

Font styles to use
Other font styles liked:
• we would like to use the font on our logo, not sure what it is though..

Requirements
Must have
• Our logo.
Nice to have
• We are open to suggestions that have to do with lighting.

```html
<!DOCTYPE html>
<html lang="en">
<head>
<meta charset="utf-8">
<title>Lumen Retrofit Partners – Business Cards</title>
<link href="https://fonts.googleapis.com/css2?family=Open+Sans:wght@400;600;700&display=swap" rel="stylesheet">
<style>
  :root {
    --stage: #3a3a3a;
    --card-black: #000000;
    --card-white: #ffffff;
    --brand-green: #1f4a27;
    --brand-green-text: #2b6b35;
    --accent-green: #5bbf4e;
    --muted-grey: #8a8a8a;
    --faint-grey: #eef0ee;
  }
  * { box-sizing: border-box; margin: 0; padding: 0; }
  html, body {
    width: 1200px; height: 864px; overflow: hidden;
    background: var(--stage);
    font-family: "Open Sans", sans-serif;
  }
  .card {
    position: absolute;
    left: 340px;
    width: 520px; height: 297px;
    overflow: hidden;
    box-shadow: 0 10px 30px rgba(0,0,0,.45);
  }
  .card--back { top: 115px; background: var(--card-black); }
  .card--front { top: 452px; background: var(--card-white); }

  .wordmark { display: flex; flex-direction: column; }
  .wordmark__name {
    display: flex; align-items: center; gap: 10px;
    font-weight: 700; letter-spacing: 2px; line-height: 1;
  }
  .wordmark__square { display: inline-block; }
  .wordmark__rule { height: 2px; background: var(--accent-green); margin-top: 6px; }
  .wordmark__legal {
    font-weight: 700; text-transform: uppercase; letter-spacing: 1.2px; margin-top: 4px;
  }

  .card--back .wordmark {
    position: absolute; left: 50%; top: 50%; transform: translate(-50%, -50%);
  }
  .card--back .wordmark__name { font-size: 56px; color: #fff; }
  .card--back .wordmark__square { width: 30px; height: 30px; background: var(--accent-green); }
  .card--back .wordmark__legal { font-size: 10.5px; color: #fff; }

  .card--front .wordmark { position: absolute; left: 42px; top: 34px; }
  .card--front .wordmark__name { font-size: 40px; color: var(--brand-green); }
  .card--front .wordmark__square { width: 22px; height: 22px; background: var(--accent-green); }
  .card--front .wordmark__legal { font-size: 8px; color: var(--brand-green); }

  .decor-block {
    position: absolute; right: 50px; top: 20px; width: 170px; height: 140px;
    background: linear-gradient(90deg, rgba(238,240,238,0) 0%, var(--faint-grey) 100%);
  }

  .person { position: absolute; left: 42px; top: 120px; }
  .person__name { font-size: 21px; font-weight: 600; color: var(--brand-green-text); line-height: 1.1; }
  .person__title { font-size: 14px; color: var(--muted-grey); }

  .band-line {
    position: absolute; left: 0; right: 0; top: 170px; height: 4px; background: var(--accent-green);
  }
  .band {
    position: absolute; left: 0; right: 0; top: 174px; bottom: 0; background: var(--brand-green);
    color: #fff;
  }
  .contacts { position: absolute; left: 42px; top: 16px; list-style: none; }
  .contacts li {
    display: flex; align-items: center; gap: 8px; font-size: 15px; line-height: 22px;
  }
  .contacts svg { width: 13px; height: 13px; flex: none; }
  .address {
    position: absolute; right: 38px; top: 44px; text-align: right; font-size: 14.5px; line-height: 21px;
  }
</style>
</head>
<body>

<section class="card card--back" aria-label="Business card back">
  <div class="wordmark">
    <div class="wordmark__name">LRP <span class="wordmark__square"></span></div>
    <div class="wordmark__rule"></div>
    <div class="wordmark__legal">Lumen Retrofit Partners, LLC</div>
  </div>
</section>

<section class="card card--front" aria-label="Business card front">
  <div class="decor-block"></div>
  <div class="wordmark">
    <div class="wordmark__name">LRP <span class="wordmark__square"></span></div>
    <div class="wordmark__rule"></div>
    <div class="wordmark__legal">Lumen Retrofit Partners, LLC</div>
  </div>

  <div class="person">
    <div class="person__name">John Smith</div>
    <div class="person__title">President</div>
  </div>

  <div class="band-line"></div>
  <div class="band">
    <ul class="contacts">
      <li>
        <svg viewBox="0 0 16 16" fill="#5bbf4e"><path d="M3.6 1.5l2.3 2.3-1.3 1.8c.9 2 2.5 3.6 4.5 4.5l1.8-1.3 2.3 2.3-1.7 2.4C6.5 13.3 2.7 9.5 1.2 4.5z"/></svg>
        01 012-345-6789
      </li>
      <li>
        <svg viewBox="0 0 16 16" fill="none" stroke="#5bbf4e" stroke-width="1.6"><rect x="4.5" y="1.5" width="7" height="13" rx="1.2"/><circle cx="8" cy="12" r=".6" fill="#5bbf4e"/></svg>
        01 012-345-6780
      </li>
      <li>
        <svg viewBox="0 0 16 16" fill="none" stroke="#5bbf4e" stroke-width="1.6"><rect x="1.5" y="3.5" width="13" height="9"/><path d="M1.5 3.5l6.5 5 6.5-5"/></svg>
        info@yourwebsite.com
      </li>
      <li>
        <svg viewBox="0 0 16 16" fill="none" stroke="#5bbf4e" stroke-width="1.4"><circle cx="8" cy="8" r="6.5"/><ellipse cx="8" cy="8" rx="2.8" ry="6.5"/><path d="M1.5 8h13"/></svg>
        yourwebsite.com
      </li>
    </ul>
    <address class="address" style="font-style:normal">
      Street Name, Suite 100<br>
      State, Zip Code, Country
    </address>
  </div>
</section>

</body>
</html>
```